2 Ridgeway Bills Motor Care Banners

Looking to have two pull up banners designed - each 33.5 x 80

First banner- Scheduled Maintenance, Diagnostics, Inspections
Voted Finest of Carrow 3 years in a row!

Second banner- Brakes, Tires, General Auto Service
Include the 3 FOC logos
2019, 2018, 2017

```html
<!DOCTYPE html>
<html lang="en">
<head>
<meta charset="utf-8">
<title>Ridgeway Bills Motor Care – Pull Up Banners</title>
<link href="https://fonts.googleapis.com/css2?family=Exo+2:wght@600;700;800&family=Montserrat:wght@700;800&display=swap" rel="stylesheet">
<style>
  :root{
    --stage:#cfcfcf;
    --paper:#ffffff;
    --navy:#0d1a3a;
    --navy-deep:#081230;
    --ink:#111111;
    --brand:#2f3f66;
    --red:#c9232b;
    --red-dark:#8e1c22;
    --white:#ffffff;
    --photo-a:#3a3f48;
    --photo-b:#151a24;
    --photo-red:#9d1d1d;
    --badge-fill:#e4e8ee;
  }
  *{box-sizing:border-box;margin:0;padding:0}
  html,body{width:1200px;height:1000px;overflow:hidden;background:var(--stage)}
  .stage{position:relative;width:1200px;height:1000px}
  .banner{position:absolute;top:63px;width:358px;height:855px;background:var(--paper);box-shadow:8px 8px 10px rgba(0,0,0,.25);overflow:hidden}
  .banner--services{left:230px}
  .banner--awards{left:647px}
  .masthead{position:absolute;left:0;top:0;width:100%;height:124px;display:flex;align-items:center;justify-content:center}
  .brand-name{font-family:"Exo 2",sans-serif;font-weight:800;color:var(--brand);font-size:34px;line-height:1.02;text-align:center}
  .panel{position:absolute;left:0;top:124px;width:100%;background:linear-gradient(180deg,var(--navy) 0%,var(--navy-deep) 100%)}
  .banner--services .panel{height:655px}
  .banner--awards .panel{height:616px}
  .hero-photo{position:absolute;left:0;top:0;width:100%;height:360px;background:linear-gradient(160deg,var(--photo-a) 0%,var(--photo-b) 45%,var(--photo-red) 62%,var(--photo-b) 80%,var(--navy) 100%)}
  .service-list{position:absolute;left:30px;top:24px;list-style:none;font-family:"Exo 2",sans-serif;font-weight:700;color:var(--white);font-size:26px;line-height:31px}
  .service-list--bars li{border-left:5px solid var(--red);padding-left:10px;margin-bottom:16px}
  .service-list--ticks{left:32px;top:26px;font-size:28px;line-height:36px}
  .service-list--ticks li{display:flex;align-items:center;gap:14px}
  .tick{width:18px;height:18px;flex:none}
  .gallery{position:absolute;left:33px;display:grid;grid-template-columns:140px 140px;grid-auto-rows:88px;gap:8px 12px}
  .banner--services .gallery{top:358px}
  .banner--awards .gallery{top:370px}
  .gallery-photo{border:2px solid var(--white)}
  .gallery-photo--wheel{background:linear-gradient(135deg,#5d7a8c,#1f2c3a)}
  .gallery-photo--shop{background:linear-gradient(180deg,#c9d6e2,#d9c9b0 60%,#8a3a2e)}
  .gallery-photo--engine{background:linear-gradient(135deg,#23324d,#3c4654)}
  .gallery-photo--tires{background:linear-gradient(90deg,#eadbc8,#3a3a3a 60%,#1c1c1c)}
  .accolade{position:absolute;left:0;top:576px;width:100%;text-align:center;font-family:"Montserrat",sans-serif;font-weight:800;text-transform:uppercase}
  .accolade-line{color:var(--white);font-size:17px}
  .accolade-highlight{color:var(--red);font-size:24px;line-height:28px}
  .web-pill{position:absolute;left:50%;transform:translateX(-50%);width:206px;height:26px;border-radius:13px;background:linear-gradient(180deg,var(--red),var(--red-dark));color:var(--white);font-family:"Montserrat",sans-serif;font-weight:700;font-size:14px;display:flex;align-items:center;justify-content:center}
  .banner--services .web-pill{top:764px}
  .banner--awards .web-pill{top:731px}
  .contact-line{position:absolute;left:0;width:100%;text-align:center;font-family:"Montserrat",sans-serif;font-weight:700;font-size:10.5px;white-space:nowrap}
  .contact-line .sep{color:var(--red);padding:0 5px}
  .banner--services .contact-line{top:802px;color:var(--ink)}
  .banner--awards .contact-line{top:577px;color:var(--white)}
  .award-row{position:absolute;left:32px;top:772px;display:flex;gap:10px}
  .award-badge{display:flex;align-items:center;gap:5px;width:96px}
  .award-seal{width:36px;height:36px;border-radius:50%;background:var(--badge-fill);border:1.5px solid var(--brand);flex:none}
  .award-text{font-family:"Montserrat",sans-serif;font-weight:800;text-transform:uppercase;line-height:1}
  .award-year{display:block;background:var(--red);color:var(--white);font-size:14px;padding:1px 3px;margin-bottom:2px;text-align:center}
  .award-name{display:block;color:var(--ink);font-size:7.5px;line-height:8.5px}
</style>
</head>
<body>
<main class="stage">

  <section class="banner banner--services" aria-label="Service banner">
    <header class="masthead"><div class="brand-name">Ridgeway Bills<br>Motor Care</div></header>
    <div class="panel">
      <div class="hero-photo" role="img" aria-label="Mechanic working under the hood of a car in a workshop"></div>
      <ul class="service-list service-list--bars">
        <li>Scheduled<br>Maintenance</li>
        <li>Diagnostics</li>
        <li>Inspections</li>
      </ul>
      <div class="gallery">
        <div class="gallery-photo gallery-photo--wheel" role="img" aria-label="Impact wrench on a wheel"></div>
        <div class="gallery-photo gallery-photo--shop" role="img" aria-label="Shop building exterior"></div>
        <div class="gallery-photo gallery-photo--engine" role="img" aria-label="Technician checking an engine"></div>
        <div class="gallery-photo gallery-photo--tires" role="img" aria-label="Stacked tires"></div>
      </div>
      <div class="accolade">
        <div class="accolade-line">Voted Finest of Carrow</div>
        <div class="accolade-highlight">3 Years in a Row!</div>
      </div>
    </div>
    <div class="web-pill">www.rbmotorcare.com</div>
    <p class="contact-line">1820 Alder Ln<span class="sep">|</span>Carrow, VA 20990<span class="sep">|</span>555-014-2276</p>
  </section>

  <section class="banner banner--awards" aria-label="Auto service banner">
    <header class="masthead"><div class="brand-name">Ridgeway Bills<br>Motor Care</div></header>
    <div class="panel">
      <div class="hero-photo" role="img" aria-label="Mechanic working under the hood of a car in a workshop"></div>
      <ul class="service-list service-list--ticks">
        <li><svg class="tick" viewBox="0 0 18 18"><circle cx="9" cy="9" r="7.5" fill="none" stroke="#c9232b" stroke-width="1.6"/><path d="M5 9l3 3 7-8" fill="none" stroke="#c9232b" stroke-width="1.8"/></svg>Auto Service</li>
        <li><svg class="tick" viewBox="0 0 18 18"><circle cx="9" cy="9" r="7.5" fill="none" stroke="#c9232b" stroke-width="1.6"/><path d="M5 9l3 3 7-8" fill="none" stroke="#c9232b" stroke-width="1.8"/></svg>Tires</li>
        <li><svg class="tick" viewBox="0 0 18 18"><circle cx="9" cy="9" r="7.5" fill="none" stroke="#c9232b" stroke-width="1.6"/><path d="M5 9l3 3 7-8" fill="none" stroke="#c9232b" stroke-width="1.8"/></svg>General</li>
        <li><svg class="tick" viewBox="0 0 18 18"><circle cx="9" cy="9" r="7.5" fill="none" stroke="#c9232b" stroke-width="1.6"/><path d="M5 9l3 3 7-8" fill="none" stroke="#c9232b" stroke-width="1.8"/></svg>Brakes</li>
      </ul>
      <div class="gallery">
        <div class="gallery-photo gallery-photo--wheel" role="img" aria-label="Impact wrench on a wheel"></div>
        <div class="gallery-photo gallery-photo--shop" role="img" aria-label="Shop building exterior"></div>
        <div class="gallery-photo gallery-photo--engine" role="img" aria-label="Technician checking an engine"></div>
        <div class="gallery-photo gallery-photo--tires" role="img" aria-label="Stacked tires"></div>
      </div>
      <p class="contact-line">1820 Alder Ln<span class="sep">|</span>Carrow, VA 20990<span class="sep">|</span>555-014-2276</p>
    </div>
    <div class="web-pill">www.rbmotorcare.com</div>
    <div class="award-row">
      <div class="award-badge"><span class="award-seal"></span><span class="award-text"><span class="award-year">2017</span><span class="award-name">Finest of<br>Carrow</span></span></div>
      <div class="award-badge"><span class="award-seal"></span><span class="award-text"><span class="award-year">2018</span><span class="award-name">Finest of<br>Carrow</span></span></div>
      <div class="award-badge"><span class="award-seal"></span><span class="award-text"><span class="award-year">2019</span><span class="award-name">Finest of<br>Carrow</span></span></div>
    </div>
  </section>

</main>
</body>
</html>
```